Start up in business consultancy needs a business card

We need the business card's layout (we have already the logo). Our business is concerned on consultancy services delivered to companies on the matter of sustainability. Business card should be enough essentials and professional style.

Side A with the following info:
logo + a space for the claim (still to identify) + website of the company

Side B with the following info:
Name of business card holder + title of the business card holder + address of the company + space for mobile number, phone number, fax number + e-mail of business card holder + graphic details around.

Target Market(s)

Business of any sector

Industry/Entity Type

Business Service

Contact Information for Business Card

Name of the company:
Pianoverde srl
Società Benefit

Address of the company:
Via Lucerna, 7
21047 - Saronno (VA)

Website:
www.pianoverde.it

Name of the BC' holder:
Luca Ferentino

Title:
Co-fondatore

Email:
luca@pianoverde.it

Mobile:
+39 348 915 2074
Phone:
+39 348 915 2074
Fax:
+39 348 915 2074

Font styles to use
Other font styles liked:
• new gothic

```html
<!DOCTYPE html>
<html lang="it">
<head>
<meta charset="utf-8">
<title>Pianoverde – Biglietto da visita</title>
<link rel="stylesheet" href="https://fonts.googleapis.com/css2?family=Poppins:wght@300;400;600&display=swap">
<style>
  :root {
    --brand-blue: #0d64a5;
    --card-white: #ffffff;
    --faint-blue: #e3eef6;
    --page-bg: #e9ebee;
    --card-shadow: rgba(0, 0, 0, 0.18);
  }
  * { box-sizing: border-box; margin: 0; padding: 0; }
  html, body {
    width: 1200px; height: 900px; overflow: hidden;
    background: var(--page-bg);
    font-family: "Poppins", "Century Gothic", sans-serif;
  }
  .canvas { position: relative; width: 1200px; height: 900px; }
  .card {
    position: absolute; width: 513px; height: 296px;
    border-radius: 24px; overflow: hidden;
    box-shadow: 0 6px 14px var(--card-shadow);
  }
  .card--front { left: 344px; top: 138px; background: var(--brand-blue); color: var(--card-white); }
  .card--back { top: 465px; background: var(--card-white); color: var(--brand-blue); }
  .card--back-a { left: 73px; }
  .card--back-b { left: 616px; }

  .brand { display: flex; align-items: center; gap: 12px; }
  .brand__dot {
    border-radius: 50%; border: 3px solid currentColor; flex: none;
  }
  .brand__name { font-weight: 400; letter-spacing: 0.2px; }

  .card--front .brand { position: absolute; left: 115px; top: 104px; }
  .card--front .brand__dot { width: 62px; height: 62px; }
  .card--front .brand__name { font-size: 27px; }
  .front__claim {
    position: absolute; top: 223px; width: 100%; text-align: center;
    font-size: 15px; font-weight: 300; letter-spacing: 7px;
  }
  .front__web {
    position: absolute; top: 256px; left: 50%; transform: translateX(-50%);
    border: 1.5px solid var(--card-white); border-radius: 14px;
    padding: 2px 12px; font-size: 12.5px; font-weight: 600;
  }

  .back__deco {
    position: absolute; left: 250px; top: -20px; width: 420px; height: 420px;
    border-radius: 50%; border: 22px solid var(--faint-blue);
  }
  .card--back .brand { position: absolute; left: 34px; top: 30px; gap: 9px; }
  .card--back .brand__dot { width: 60px; height: 60px; border-width: 2.5px; }
  .card--back .brand__name { font-size: 20px; }

  .holder { position: absolute; left: 35px; font-size: 15.5px; }
  .holder__name { font-weight: 600; }
  .holder__sep { font-weight: 300; margin: 0 3px; font-size: 14px; }
  .holder__role { font-weight: 300; font-size: 14px; }
  .card--back-a .holder { top: 148px; }
  .card--back-b .holder { top: 177px; }

  .company { font-size: 12.5px; font-weight: 600; line-height: 18px; }
  .contacts { list-style: none; font-size: 13px; font-weight: 300; line-height: 18.5px; }
  .contacts li { display: flex; align-items: center; gap: 6px; }
  .contacts svg { width: 12px; height: 12px; flex: none; }
  .address { font-size: 13px; font-weight: 300; line-height: 18.5px; }

  .card--back-a .details { position: absolute; left: 35px; top: 178px; }
  .card--back-b .contacts { position: absolute; left: 35px; top: 216px; }
  .card--back-b .contacts li { gap: 9px; }
  .card--back-b .office { position: absolute; left: 341px; top: 239px; line-height: 18px; }
</style>
</head>
<body>
<svg width="0" height="0" style="position:absolute" aria-hidden="true">
  <defs>
    <symbol id="icon-mobile" viewBox="0 0 12 12"><circle cx="6" cy="6" r="6" fill="currentColor"/><rect x="3.8" y="2.3" width="4.4" height="7.4" rx="0.8" fill="#fff"/><rect x="4.5" y="3.1" width="3" height="4.6" fill="currentColor"/></symbol>
    <symbol id="icon-phone" viewBox="0 0 12 12"><circle cx="6" cy="6" r="6" fill="currentColor"/><path d="M2.6 5.2c0-1.3 1.6-2 3.4-2s3.4.7 3.4 2l-1.3.4-.3-1H4.2l-.3 1z" fill="#fff"/><rect x="3.5" y="6" width="5" height="2.6" rx="0.6" fill="#fff"/></symbol>
    <symbol id="icon-fax" viewBox="0 0 12 12"><circle cx="6" cy="6" r="6" fill="currentColor"/><rect x="4" y="2.6" width="4" height="2.4" fill="#fff"/><rect x="2.8" y="5.3" width="6.4" height="3" rx="0.6" fill="#fff"/><rect x="4" y="7.4" width="4" height="2" fill="#fff" stroke="currentColor" stroke-width="0.5"/></symbol>
    <symbol id="icon-mail" viewBox="0 0 12 12"><circle cx="6" cy="6" r="6" fill="currentColor"/><rect x="2.7" y="3.7" width="6.6" height="4.6" rx="0.6" fill="#fff"/><path d="M2.9 4l3.1 2.4L9.1 4" fill="none" stroke="currentColor" stroke-width="0.8"/></symbol>
  </defs>
</svg>

<main class="canvas">
  <section class="card card--front" aria-label="Fronte">
    <div class="brand"><span class="brand__dot"></span><span class="brand__name">pianoverde</span></div>
    <p class="front__claim">SOCIETÀ BENEFIT</p>
    <p class="front__web">www.pianoverde.it</p>
  </section>

  <section class="card card--back card--back-a" aria-label="Retro, variante A">
    <div class="back__deco" aria-hidden="true"></div>
    <div class="brand"><span class="brand__dot"></span><span class="brand__name">pianoverde</span></div>
    <p class="holder"><span class="holder__name">Luca Ferentino</span><span class="holder__sep">|</span><span class="holder__role">Co-fondatore</span></p>
    <div class="details">
      <p class="company">Pianoverde srl</p>
      <ul class="contacts">
        <li><svg><use href="#icon-mobile"/></svg>+39 348 915 2074</li>
        <li><svg><use href="#icon-phone"/></svg>+39 348 915 2074</li>
        <li><svg><use href="#icon-fax"/></svg>+39 348 915 2074</li>
        <li><svg><use href="#icon-mail"/></svg>luca@pianoverde.it</li>
      </ul>
      <p class="address">Via Lucerna, 7, 21047 - Saronno (VA)</p>
    </div>
  </section>

  <section class="card card--back card--back-b" aria-label="Retro, variante B">
    <div class="back__deco" aria-hidden="true"></div>
    <div class="brand"><span class="brand__dot"></span><span class="brand__name">pianoverde</span></div>
    <p class="holder"><span class="holder__name">Luca Ferentino</span><span class="holder__sep">|</span><span class="holder__role">Co-fondatore</span></p>
    <ul class="contacts">
      <li><svg><use href="#icon-mobile"/></svg>+39 348 915 2074</li>
      <li><svg><use href="#icon-phone"/></svg>+39 348 915 2074</li>
      <li><svg><use href="#icon-fax"/></svg>+39 348 915 2074</li>
      <li><svg><use href="#icon-mail"/></svg>luca@pianoverde.it</li>
    </ul>
    <div class="office">
      <p class="company">Pianoverde srl</p>
      <p class="address">Via Lucerna, 7<br>21047 - Saronno (VA)</p>
    </div>
  </section>
</main>
</body>
</html>
```